Looking for a dynamic business card for a pizzeria.

A business card with our food, logo, and space for name, title, email, website, phone. The card should convey quality, unique, amazing. On the front, I envision food photo or photos with the owners names and contact information. On the back, more food with locations, website, facebook, twitter, instagram icons. It should look polished, not cartoonish, or plain.
Target Market(s)
upscale, local food buyers, 30-50 years in age.
Industry/Entity Type
Restaurant
Contact Information for Business Card
Business Name: Crustella, LLC
Website: www.crustellaovens.com
Back:
2 locations: (can list on the back of card)
1. Fairhaven
2736 Marlow Street
Bellingham, WA 98225
360-555-0143
2. Alabama Hill
1187 Pelham Street
Bellingham, WA 98229
360-555-0187
front:
EDITABLE space for
Business name
Person's Name
title
2nd title
Email address
cell-phone number
Requirements
Must have
- logo
- my food photo or photos (no watermarks showing)
- locations on back
- Person contact information on front
- full bleed

```html
<!DOCTYPE html>
<html lang="en">
<head>
<meta charset="utf-8">
<title>Crustella business card</title>
<link rel="stylesheet" href="https://fonts.googleapis.com/css2?family=Montserrat:wght@400;500;600;700&display=swap">
<style>
  :root {
    --stage: #d9d6d1;
    --card: #eeeeec;
    --card-edge: #ffffff;
    --band: #1e1e20;
    --band-light: #2e2e31;
    --rim: #bfc0c2;
    --ink: #2f2f31;
    --muted: #5a5a5d;
    --paper: #f4f4f4;
    --brand-green: #3e7a46;
    --brand-red: #c9423a;
  }
  * { box-sizing: border-box; margin: 0; padding: 0; }
  html, body { width: 1200px; height: 1013px; overflow: hidden; }
  body {
    background: var(--stage);
    font-family: "Montserrat", Arial, sans-serif;
    position: relative;
  }
  .card {
    position: absolute;
    left: 283px;
    width: 636px;
    height: 365px;
    background: var(--card);
    border: 2px solid var(--card-edge);
    border-radius: 20px;
    overflow: hidden;
    box-shadow: 0 10px 30px rgba(0,0,0,0.12);
  }
  .card--front { top: 115px; }
  .card--back { top: 528px; }

  .brand {
    position: absolute;
    left: 0; right: 0;
    top: 58px;
    display: flex;
    justify-content: center;
    align-items: center;
    gap: 14px;
  }
  .brand__name {
    font-weight: 700;
    font-size: 46px;
    letter-spacing: 1px;
    color: var(--brand-green);
  }
  .brand__dot {
    width: 52px; height: 52px;
    border-radius: 50%;
    background: var(--brand-red);
  }

  .band {
    position: absolute;
    left: 0; right: 0;
    background: linear-gradient(180deg, var(--band-light), var(--band) 30%, var(--band));
    border-top: 3px solid var(--rim);
    border-bottom: 3px solid var(--rim);
  }
  .card--front .band { top: 168px; height: 162px; }
  .card--back .band { top: 168px; height: 134px; }

  .band__notch {
    position: absolute;
    left: 124px; top: 165px;
    width: 22px; height: 14px;
  }

  .person {
    position: absolute;
    left: 0; width: 300px;
    top: 55px;
    text-align: center;
    color: var(--paper);
  }
  .person__name { font-size: 21px; font-weight: 500; letter-spacing: 1px; }
  .person__title { font-size: 15px; margin-top: 6px; }

  .band__divider {
    position: absolute;
    left: 306px; top: 22px;
    width: 1px; height: 118px;
    background: #9a9a9c;
  }
  .contacts {
    position: absolute;
    left: 330px; top: 24px;
    list-style: none;
    color: var(--paper);
    font-size: 13px;
  }
  .contacts li {
    display: flex; align-items: center; gap: 10px;
    height: 29px;
  }
  .contacts svg { width: 15px; height: 15px; flex: none; }

  .website {
    position: absolute;
    left: 0; right: 0;
    bottom: 10px;
    text-align: center;
    font-size: 17px;
    font-weight: 500;
    letter-spacing: 1.5px;
    color: var(--ink);
  }

  .locations {
    position: absolute;
    left: 0; right: 0; top: 26px;
    display: flex;
    justify-content: center;
    gap: 0;
  }
  .location {
    width: 260px;
    padding: 0 24px;
    color: var(--ink);
    font-size: 13px;
    line-height: 21px;
  }
  .location + .location { border-left: 1px solid #b5b5b7; }
  .location__name {
    display: flex; align-items: center; gap: 8px;
    font-size: 16px;
    font-weight: 600;
    color: var(--brand-green);
    margin-bottom: 6px;
  }
  .location__name svg { width: 14px; height: 14px; flex: none; }
  .location__phone { font-weight: 600; color: var(--ink); }

  .gallery {
    position: absolute;
    left: 30px; right: 30px; top: 10px;
    display: flex;
    justify-content: space-between;
  }
  .gallery__photo {
    width: 128px; height: 110px;
    border: 4px solid #ffffff;
    border-radius: 14px;
  }
  .gallery__photo--slices { background: linear-gradient(140deg, #e9d9c4, #c2583a 55%, #7a2e1d); }
  .gallery__photo--wraps { background: linear-gradient(150deg, #c9b07a, #a8712e 50%, #5b7a34); }
  .gallery__photo--tray { background: linear-gradient(160deg, #6e4a2c, #c2562c 50%, #e3a64d); }
  .gallery__photo--dough { background: linear-gradient(140deg, #3a2a22, #d8b479 55%, #efe0b8); }

  .back-footer {
    position: absolute;
    left: 0; right: 0;
    top: 305px; height: 56px;
    display: flex;
    justify-content: center;
    align-items: center;
    gap: 26px;
  }
  .back-footer .website { position: static; }
  .social { display: flex; gap: 8px; list-style: none; }
  .social li {
    width: 22px; height: 22px;
    border-radius: 50%;
    background: var(--band);
  }
</style>
</head>
<body>

<section class="card card--front" aria-label="Card front">
  <div class="brand">
    <span class="brand__name">CRUSTELLA</span>
    <span class="brand__dot"></span>
  </div>

  <div class="band">
    <div class="person">
      <p class="person__name">MARCO BELLANDI</p>
      <p class="person__title">Managing Director</p>
    </div>
    <span class="band__divider"></span>
    <ul class="contacts">
      <li>
        <svg viewBox="0 0 16 16"><circle cx="8" cy="8" r="8" fill="#f4f4f4"/><path d="M5.2 4.2l1.4-.4.9 2-1 .8c.5 1.1 1.3 1.9 2.4 2.4l.8-1 2 .9-.4 1.4c-3.3.2-6.3-2.8-6.1-6.1z" fill="#1e1e20"/></svg>
        360-555-0143
      </li>
      <li>
        <svg viewBox="0 0 16 16"><circle cx="8" cy="8" r="8" fill="#f4f4f4"/><path d="M5.2 4.2l1.4-.4.9 2-1 .8c.5 1.1 1.3 1.9 2.4 2.4l.8-1 2 .9-.4 1.4c-3.3.2-6.3-2.8-6.1-6.1z" fill="#1e1e20"/></svg>
        360-555-0187
      </li>
      <li>
        <svg viewBox="0 0 16 16"><circle cx="8" cy="8" r="8" fill="#f4f4f4"/><rect x="4" y="5" width="8" height="6" fill="#1e1e20"/><path d="M4 5l4 3.4L12 5" stroke="#f4f4f4" stroke-width="1" fill="none"/></svg>
        marco@crustellaovens.com
      </li>
      <li>
        <svg viewBox="0 0 16 16"><circle cx="8" cy="8" r="8" fill="#f4f4f4"/><path d="M8 3.5a3 3 0 0 1 3 3c0 2.2-3 5.8-3 5.8S5 8.7 5 6.5a3 3 0 0 1 3-3z" fill="#1e1e20"/><circle cx="8" cy="6.5" r="1.1" fill="#f4f4f4"/></svg>
        2736 Marlow Street, Bellingham WA
      </li>
    </ul>
  </div>
  <svg class="band__notch" viewBox="0 0 22 14"><path d="M0 0h22L11 14z" fill="#eeeeec"/></svg>

  <p class="website">www.crustellaovens.com</p>
</section>

<section class="card card--back" aria-label="Card back">
  <div class="locations">
    <div class="location">
      <p class="location__name">
        <svg viewBox="0 0 16 16"><path d="M8 1a4.5 4.5 0 0 1 4.5 4.5C12.5 9 8 15 8 15S3.5 9 3.5 5.5A4.5 4.5 0 0 1 8 1z" fill="#c9423a"/><circle cx="8" cy="5.5" r="1.6" fill="#eeeeec"/></svg>
        Fairhaven
      </p>
      <p>2736 Marlow Street</p>
      <p>Bellingham, WA 98225</p>
      <p class="location__phone">360-555-0143</p>
    </div>
    <div class="location">
      <p class="location__name">
        <svg viewBox="0 0 16 16"><path d="M8 1a4.5 4.5 0 0 1 4.5 4.5C12.5 9 8 15 8 15S3.5 9 3.5 5.5A4.5 4.5 0 0 1 8 1z" fill="#c9423a"/><circle cx="8" cy="5.5" r="1.6" fill="#eeeeec"/></svg>
        Alabama Hill
      </p>
      <p>1187 Pelham Street</p>
      <p>Bellingham, WA 98229</p>
      <p class="location__phone">360-555-0187</p>
    </div>
  </div>

  <div class="band">
    <div class="gallery">
      <div class="gallery__photo gallery__photo--slices" role="img" aria-label="Photo of pizza slices on a plate"></div>
      <div class="gallery__photo gallery__photo--wraps" role="img" aria-label="Photo of folded flatbread with fillings"></div>
      <div class="gallery__photo gallery__photo--tray" role="img" aria-label="Photo of pizzas baking in an oven"></div>
      <div class="gallery__photo gallery__photo--dough" role="img" aria-label="Photo of fresh pizza dough being prepared"></div>
    </div>
  </div>

  <div class="back-footer">
    <p class="website">www.crustellaovens.com</p>
    <ul class="social" aria-label="Social media">
      <li aria-label="Social profile one"></li>
      <li aria-label="Social profile two"></li>
      <li aria-label="Social profile three"></li>
    </ul>
  </div>
</section>

</body>
</html>
```